Start up needs juice bottle label design

Bramblecrest Citrus Co juice company needs juice bottle label design for all natural lemonades, teas, smoothies and cold-pressed juice. We would like the design to have a space for multiple flavors or custom recipes for special orders. Below is the company logo.

Target Market(s)

On-the-go Health conscious

```html
<!DOCTYPE html>
<html lang="en">
<head>
<meta charset="utf-8">
<title>Bramblecrest Citrus Co — Bottle Labels</title>
<link href="https://fonts.googleapis.com/css2?family=Sniglet:wght@400;800&family=Montserrat:wght@400&display=swap" rel="stylesheet">
<style>
  :root{
    --backdrop:#e6e6e6;
    --white:#ffffff;
    --yellow:#ffc600;
    --pale-yellow:#f7eb80;
    --pink:#e0245e;
    --blue:#00cfff;
    --green:#9ecf52;
    --dark-green:#56a158;
    --orange:#ffaa00;
    --ink:#1a1a1a;
  }
  *{box-sizing:border-box;margin:0;padding:0}
  html,body{width:1200px;height:1200px;overflow:hidden}
  body{background:var(--backdrop);font-family:"Sniglet",sans-serif}
  .label-row{
    position:absolute;left:30px;top:348px;
    display:flex;gap:60px;
  }
  .label{
    position:relative;width:240px;height:504px;
    border-radius:28px;overflow:hidden;background:var(--white);
  }
  .label svg{position:absolute;inset:0;width:100%;height:100%}
  .brand-name{
    position:absolute;top:56px;left:0;right:0;
    text-align:center;font-size:24px;line-height:1.1;font-weight:800;
    color:var(--pink);padding:0 18px;
  }
  .flavour-name{
    position:absolute;left:0;right:0;top:206px;
    text-align:center;font-size:30px;line-height:1.25;font-weight:400;
    color:var(--white);
  }
  .flavour-name.single{top:222px;font-size:44px}
  .flavour-name.dark{color:var(--ink)}
  .volume{
    position:absolute;left:0;right:0;bottom:36px;
    text-align:center;font-family:"Montserrat",sans-serif;font-size:17px;color:var(--ink);
  }
</style>
</head>
<body>
<main class="label-row">

  <article class="label label--lemonade">
    <svg viewBox="0 0 240 504" aria-hidden="true">
      <path d="M0 148 Q20 182 40 164 Q60 182 80 164 Q100 182 120 164 Q140 182 160 164 Q180 182 200 164 Q220 182 240 148 L240 504 L0 504 Z" fill="var(--yellow)"/>
      <rect x="0" y="196" width="108" height="46" rx="14" fill="var(--green)" transform="translate(-20 0)"/>
      <g role="img" aria-label="Flat illustration of a lemon with leaves among pink, blue and green shapes">
        <defs><linearGradient id="lemonArt" x1="0" y1="0" x2="1" y2="1"><stop offset="0" stop-color="var(--pink)"/><stop offset=".45" stop-color="var(--yellow)"/><stop offset=".75" stop-color="var(--blue)"/><stop offset="1" stop-color="var(--green)"/></linearGradient></defs>
        <rect x="0" y="300" width="240" height="204" fill="url(#lemonArt)"/>
      </g>
    </svg>
    <p class="brand-name">Bramblecrest Citrus Co</p>
    <h2 class="flavour-name">NaTuRaL<br>LeMoNaDes</h2>
    <p class="volume">250ml</p>
  </article>

  <article class="label label--smoothie">
    <svg viewBox="0 0 240 504" aria-hidden="true">
      <path d="M0 148 Q20 182 40 164 Q60 182 80 164 Q100 182 120 164 Q140 182 160 164 Q180 182 200 164 Q220 182 240 148 L240 504 L0 504 Z" fill="var(--pale-yellow)"/>
      <rect x="-20" y="196" width="128" height="46" rx="14" fill="var(--yellow)"/>
      <g role="img" aria-label="Flat illustration of a banana and an orange over blue and green shapes">
        <defs><linearGradient id="bananaArt" x1="0" y1="0" x2="1" y2="1"><stop offset="0" stop-color="var(--blue)"/><stop offset=".5" stop-color="var(--dark-green)"/><stop offset=".8" stop-color="var(--orange)"/><stop offset="1" stop-color="var(--yellow)"/></linearGradient></defs>
        <rect x="0" y="300" width="240" height="204" fill="url(#bananaArt)"/>
      </g>
    </svg>
    <p class="brand-name">Bramblecrest Citrus Co</p>
    <h2 class="flavour-name dark">Banana<br>Smothies</h2>
    <p class="volume">250ml</p>
  </article>

  <article class="label label--tea">
    <svg viewBox="0 0 240 504" aria-hidden="true">
      <path d="M0 148 Q20 182 40 164 Q60 182 80 164 Q100 182 120 164 Q140 182 160 164 Q180 182 200 164 Q220 182 240 148 L240 504 L0 504 Z" fill="var(--green)"/>
      <g role="img" aria-label="Flat illustration of tea leaves over orange, yellow and pink shapes">
        <defs><linearGradient id="teaArt" x1="0" y1="0" x2="1" y2="1"><stop offset="0" stop-color="var(--yellow)"/><stop offset=".5" stop-color="var(--orange)"/><stop offset="1" stop-color="var(--pink)"/></linearGradient></defs>
        <rect x="0" y="300" width="240" height="204" fill="url(#teaArt)"/>
      </g>
    </svg>
    <p class="brand-name">Bramblecrest Citrus Co</p>
    <h2 class="flavour-name single">Theas</h2>
    <p class="volume">250ml</p>
  </article>

  <article class="label label--juice">
    <svg viewBox="0 0 240 504" aria-hidden="true">
      <path d="M0 148 Q20 182 40 164 Q60 182 80 164 Q100 182 120 164 Q140 182 160 164 Q180 182 200 164 Q220 182 240 148 L240 504 L0 504 Z" fill="var(--pink)"/>
      <rect x="-20" y="196" width="128" height="46" rx="14" fill="var(--orange)"/>
      <g role="img" aria-label="Flat illustration of an apple and an orange over green shapes">
        <defs><linearGradient id="juiceArt" x1="0" y1="0" x2="1" y2="1"><stop offset="0" stop-color="var(--dark-green)"/><stop offset=".5" stop-color="var(--green)"/><stop offset=".75" stop-color="var(--orange)"/><stop offset="1" stop-color="var(--pink)"/></linearGradient></defs>
        <rect x="0" y="300" width="240" height="204" fill="url(#juiceArt)"/>
      </g>
    </svg>
    <p class="brand-name">Bramblecrest Citrus Co</p>
    <h2 class="flavour-name">PreSsed<br>JuiCe</h2>
    <p class="volume">250ml</p>
  </article>

</main>
</body>
</html>
```